Manifesto

I want a manifesto with the following five manifestos for our Not for Profit

- We are a For-purpose organisation
- Every service we offer is free
- Every product we sell funds our services
- Every financial transaction is transparent
- Our service is for the greater good
- Our purpose is always to serve the people
- We are a for purpose organisation

Its to go with this website logo/look/feel www.brightlantern.co.nz

Two attachments:

1. I quite like this look/feel of a manifesto (see attached), I want something clean, professional but I also quite like either Retro modern look feel also like a fresh, and uplifting as its for sick people coming to see us and our funds where anyone buys a product are used for helping those who are sick with healing......so needs something conveyed that is fresh, uplifing yet professional.
2. This attachment is how I wrote this down when inspired of how I wanted Bright Lantern to operate. This is our values chart. It has to say

Also check out our website for our logo, look etc.. it doesnt have to be the same but red somewhere would link back to logo. www.brightlantern.co.nz .

Industry/Entity Type

Financial

```html
<!DOCTYPE html>
<html lang="en">
<head>
<meta charset="utf-8">
<title>Bright Lantern Manifesto</title>
<link rel="stylesheet" href="https://fonts.googleapis.com/css2?family=Arvo:wght@700&family=Handlee&family=Ultra&family=Cutive&family=Libre+Baskerville&family=Caveat:wght@500&family=Questrial&family=Poppins:wght@600&family=Chewy&family=Courier+Prime&display=swap">
<style>
  :root {
    --ink: #111111;
    --red: #e8141b;
    --grey: #8a8a8a;
    --mid-grey: #666666;
    --paper: #ffffff;
  }
  html, body {
    margin: 0;
    padding: 0;
    overflow: hidden;
    background: var(--paper);
  }
  .manifesto {
    position: relative;
    width: 848px;
    height: 1200px;
    background: var(--paper);
    color: var(--ink);
    overflow: hidden;
  }
  .line {
    position: absolute;
    margin: 0;
    white-space: nowrap;
    line-height: 1;
  }
  .tagline {
    left: 0;
    width: 848px;
    text-align: center;
    font-family: "Questrial", sans-serif;
    font-size: 23px;
    letter-spacing: 2px;
    color: var(--grey);
  }
  .tagline--top { top: 38px; }
  .tagline--bottom { top: 1138px; }

  .slab { font-family: "Arvo", serif; font-weight: 700; }
  .hand { font-family: "Handlee", cursive; }
  .script-red { font-family: "Chewy", cursive; color: var(--red); }
  .stamp { font-family: "Ultra", serif; }
  .typewriter { font-family: "Cutive", serif; color: #333; }
  .classic { font-family: "Libre Baskerville", serif; }
  .narrow-hand { font-family: "Caveat", cursive; }
  .geo { font-family: "Poppins", sans-serif; font-weight: 600; }
  .clean { font-family: "Questrial", sans-serif; }

  .pledge-free { left: 38px; top: 105px; }
  .pledge-free .slab { font-size: 46px; }
  .pledge-free .hand { font-size: 30px; }
  .pledge-free .script-red { font-size: 118px; letter-spacing: 4px; }

  .pledge-product { left: 78px; top: 268px; }
  .pledge-product .stamp { font-size: 56px; }
  .pledge-product .typewriter { font-size: 42px; }

  .pledge-funds { left: 78px; top: 345px; }
  .pledge-funds .funds { font-family: "Caveat", cursive; color: var(--red); font-size: 56px; }
  .pledge-funds .hand { font-size: 44px; }

  .pledge-transparent { left: 197px; top: 450px; }
  .pledge-transparent .classic { font-size: 50px; }
  .pledge-transparent .narrow-hand { font-size: 38px; }

  .transparent-word { left: 197px; top: 510px; font-family: "Ultra", serif; font-size: 80px; color: var(--grey); letter-spacing: 1px; }

  .greater-lead { left: 38px; top: 662px; font-size: 44px; }
  .greater-good { left: 38px; top: 712px; font-size: 84px; }
  .greater-good .muted { color: var(--mid-grey); }

  .purpose { left: 38px; top: 860px; }
  .purpose .clean { font-size: 50px; }
  .purpose .stamp { font-size: 66px; }

  .serve { left: 200px; top: 946px; font-family: "Handlee", cursive; font-style: italic; font-size: 56px; letter-spacing: 3px; color: #222; }
  .serve .people { color: var(--red); }

  .footer-note { top: 1022px; font-size: 16px; color: var(--ink); }
  .footer-note--motto { left: 40px; font-family: "Questrial", sans-serif; }
  .footer-note--web { right: 40px; font-family: "Courier Prime", monospace; }
</style>
</head>
<body>
<main class="manifesto">
  <p class="line tagline tagline--top">WE ARE A FOR PURPOSE ORGANISATION</p>

  <p class="line pledge-free"><span class="slab">Every</span> <span class="hand">service we offer is</span> <span class="script-red">free</span></p>

  <p class="line pledge-product"><span class="stamp">EVERY</span> <span class="typewriter">product we sell</span></p>
  <p class="line pledge-funds"><span class="funds">funds</span> <span class="hand">our services</span></p>

  <p class="line pledge-transparent"><span class="classic">EVERY</span> <span class="narrow-hand">financial transaction is</span></p>
  <p class="line transparent-word">transparent</p>

  <p class="line greater-lead hand">Our service is for</p>
  <p class="line greater-good geo"><span class="muted">the</span> greater good</p>

  <p class="line purpose"><span class="clean">Our purpose is</span> <span class="stamp">ALWAYS</span></p>
  <p class="line serve">to serve the <span class="people">people</span></p>

  <p class="line footer-note footer-note--motto">Your health, Your Life, Your Way!</p>
  <p class="line footer-note footer-note--web">www.brightlantern.co.nz</p>

  <p class="line tagline tagline--bottom">WE ARE A FOR PURPOSE ORGANISATION</p>
</main>
</body>
</html>
```